Larkspur Stillness

Logo picture and I want it to say

yoga. meditation. sound healing

small sweet classes

Larkspur-stillness.com

2740 West Hollander Ave Suite K
Brightwater Cove ca 95099

```html
<!DOCTYPE html>
<html lang="en">
<head>
<meta charset="utf-8">
<title>Larkspur Stillness — Flyer</title>
<link rel="stylesheet" href="https://fonts.googleapis.com/css2?family=Marcellus&family=Open+Sans:wght@500&display=swap">
<style>
  :root {
    --sky: #7fcfec;
    --blush: #dfb9da;
    --violet-deep: #a35fd6;
    --violet-mid: #9277d8;
    --violet-soft: #ac94df;
    --pill: #6c5aa8;
    --ink: #2b2540;
    --white: #ffffff;
    --photo-top: #9fb48e;
    --photo-mid: #c9c6b4;
    --photo-low: #3b3733;
  }
  html, body {
    margin: 0;
    padding: 0;
    width: 990px;
    height: 1200px;
    overflow: hidden;
    background: #ece9f1;
  }
  .flyer {
    position: relative;
    width: 990px;
    height: 1200px;
    overflow: hidden;
    font-family: "Marcellus", serif;
  }
  .flyer__shapes {
    position: absolute;
    inset: 0;
    width: 990px;
    height: 1200px;
    display: block;
  }
  .brand {
    position: absolute;
    left: 652px;
    top: 470px;
    width: 232px;
    height: 232px;
    border: 2px solid var(--white);
    border-radius: 50%;
    box-sizing: border-box;
    display: flex;
    align-items: center;
    justify-content: center;
  }
  .brand__name {
    color: var(--white);
    font-family: "Marcellus", serif;
    font-size: 25px;
    text-align: center;
    line-height: 1.15;
  }
  .headline {
    position: absolute;
    left: 0;
    width: 990px;
    top: 715px;
    margin: 0;
    text-align: center;
    color: var(--white);
    font-family: "Marcellus", serif;
    font-weight: 400;
    font-size: 84px;
    line-height: 100px;
    letter-spacing: 0.5px;
  }
  .tagline {
    position: absolute;
    left: 112px;
    top: 931px;
    width: 766px;
    height: 60px;
    border-radius: 30px;
    background: var(--pill);
    box-shadow: 0 8px 10px rgba(70, 40, 110, 0.25);
    color: var(--white);
    font-family: "Marcellus", serif;
    font-size: 42px;
    font-weight: 700;
    letter-spacing: 1px;
    display: flex;
    align-items: center;
    justify-content: center;
  }
  .contact {
    position: absolute;
    left: 562px;
    top: 1062px;
    margin: 0;
    padding: 0;
    list-style: none;
    font-family: "Open Sans", sans-serif;
    font-weight: 500;
    font-size: 17px;
    line-height: 25px;
    color: var(--ink);
  }
  .contact__item {
    display: flex;
    align-items: flex-start;
    margin-bottom: 7px;
  }
  .contact__icon {
    width: 20px;
    height: 20px;
    margin-right: 8px;
    margin-top: 2px;
    flex: none;
  }
</style>
</head>
<body>
<main class="flyer">
  <svg class="flyer__shapes" viewBox="0 0 1205 1560" preserveAspectRatio="none">
    <defs>
      <linearGradient id="photoTone" x1="0" y1="0" x2="0" y2="1">
        <stop offset="0" stop-color="var(--photo-top)"/>
        <stop offset="0.4" stop-color="var(--photo-mid)"/>
        <stop offset="0.75" stop-color="var(--photo-low)"/>
        <stop offset="1" stop-color="#7d6c5c"/>
      </linearGradient>
      <linearGradient id="violetWash" x1="0" y1="1" x2="1" y2="0">
        <stop offset="0" stop-color="var(--violet-deep)"/>
        <stop offset="0.5" stop-color="var(--violet-mid)"/>
        <stop offset="1" stop-color="var(--violet-soft)"/>
      </linearGradient>
    </defs>
    <rect class="photo" x="0" y="0" width="1205" height="900" fill="url(#photoTone)" role="img" aria-label="Photo of a small yoga class sitting cross-legged with hands in prayer position in a bright studio with large windows"/>
    <path class="wave wave--sky-top" d="M1205 367 C1050 360 950 440 850 520 C760 590 700 640 620 690 L620 1000 L1205 1000 Z" fill="var(--sky)"/>
    <path class="wave wave--blush-top" d="M0 685 C200 630 450 640 665 672 L700 1000 L0 1000 Z" fill="var(--blush)"/>
    <path class="wave wave--violet" d="M0 860 C250 885 450 785 640 682 C800 592 960 500 1205 500 L1205 1560 L0 1560 Z" fill="url(#violetWash)"/>
    <path class="wave wave--blush-bottom" d="M480 1460 C700 1330 950 1262 1205 1270 L1205 1560 L480 1560 Z" fill="var(--blush)"/>
    <path class="wave wave--sky-bottom" d="M0 1350 C120 1360 230 1440 380 1460 C420 1463 450 1460 470 1455 C380 1490 330 1520 280 1560 L0 1560 Z" fill="var(--sky)"/>
    <path class="wave wave--white" d="M280 1560 C500 1420 700 1320 900 1315 C1030 1312 1130 1360 1205 1410 L1205 1560 Z" fill="var(--white)"/>
  </svg>

  <div class="brand">
    <span class="brand__name">Larkspur Stillness</span>
  </div>

  <h1 class="headline">Yoga. Meditation.<br>Sound Healing</h1>

  <div class="tagline">SMALL SWEET CLASSES</div>

  <ul class="contact">
    <li class="contact__item">
      <svg class="contact__icon" viewBox="0 0 20 20"><circle cx="10" cy="10" r="10" fill="var(--pill)"/><path d="M10 4.5a3.2 3.2 0 0 0-3.2 3.2c0 2.4 3.2 6 3.2 6s3.2-3.6 3.2-6A3.2 3.2 0 0 0 10 4.5z" fill="none" stroke="#fff" stroke-width="1.3"/><circle cx="10" cy="7.7" r="1.1" fill="#fff"/><path d="M6.5 15.5h7" stroke="#fff" stroke-width="1.2"/></svg>
      <span>2740 West Hollander Ave Suite K<br>Brightwater Cove ca 95099</span>
    </li>
    <li class="contact__item">
      <svg class="contact__icon" viewBox="0 0 20 20"><circle cx="10" cy="10" r="10" fill="var(--pill)"/><circle cx="10" cy="10" r="5.5" fill="none" stroke="#fff" stroke-width="1.2"/><path d="M8 7.5c0 2.5 1.8 4.5 4.3 4.8l.6-1-1.3-.8-.6.6c-.9-.4-1.6-1.2-1.9-2l.6-.6-.8-1.3z" fill="#fff"/></svg>
      <span>555-246-0187</span>
    </li>
    <li class="contact__item">
      <svg class="contact__icon" viewBox="0 0 20 20"><circle cx="10" cy="10" r="10" fill="var(--pill)"/><circle cx="10" cy="10" r="5.5" fill="none" stroke="#fff" stroke-width="1.1"/><ellipse cx="10" cy="10" rx="2.3" ry="5.5" fill="none" stroke="#fff" stroke-width="1.1"/><path d="M4.5 10h11" stroke="#fff" stroke-width="1.1"/></svg>
      <span>Larkspur-stillness.com</span>
    </li>
  </ul>
</main>
</body>
</html>
```